Granite Ridge College-Pinecrest Welcome Week

I am the Student Activities Coordinator at Granite Ridge College-Pinecrest. For Welcome Week 2013, I need a standard poster 24x36 with the list of events happening. Our theme is based on the popular Friday Late Laughs video "We Got a Kite"
http://www.vidtrove.example/clip/Q4mZp8sLwTe
Our theme is:
We're at the 'Crest!
Welcome Week 2013
Graphics on the poster should reflect popular images/designs of FLL We Got a Kite. However, the boat should be a steamboat instead of the yacht image.
Unfortunately, I have a lot of text to fit on the poster. Traditionally we go with 3 margins listing events. I'm attaching the word document of events and our logo to this proposal. I'll also attach a few google images of "We Got a Kite" that align with the type of theme I'm looking for.
One last thing, our logo contains mountains listing all of the different campuses. Remove the campus names and mountains all together. Use simply the Colorado flag C and "Granite Ridge College".
Thanks for considering this brief!
Glen
Target Market(s)
Our college students love to ski and snowboard. In fact, one of our degrees is "Alpine Slope Commerce". Their ages are 18-22.
Industry/Entity Type
Events
Look and feel

```html
<!DOCTYPE html>
<html lang="en">
<head>
<meta charset="utf-8">
<title>Welcome Week 2013 – Granite Ridge College</title>
<link href="https://fonts.googleapis.com/css2?family=Lilita+One&family=Roboto+Condensed:wght@400;700&display=swap" rel="stylesheet">
<style>
:root{
  --frame:#2b5f9e;
  --sky-top:#9fd3f3;
  --sky-mid:#d9eefa;
  --water:#2e86c8;
  --water-deep:#1c5f9c;
  --card:#fbe56a;
  --card-edge:#e3c53a;
  --day:#d2321f;
  --ink:#1b1b1b;
  --title:#123f86;
  --white:#ffffff;
}
*{box-sizing:border-box;margin:0;padding:0}
html,body{width:828px;height:1200px;overflow:hidden;background:#fff}
.poster{position:relative;width:828px;height:1200px;border:14px solid var(--frame);
  background:linear-gradient(180deg,var(--sky-top) 0%,var(--sky-mid) 45%,#bfe2f6 62%,var(--water) 72%,var(--water-deep) 100%);
  font-family:"Roboto Condensed",Arial,sans-serif;color:var(--ink);overflow:hidden}
.brand{position:absolute;left:28px;top:22px;display:flex;align-items:center;gap:8px;
  background:var(--title);padding:8px 12px;color:var(--white);font-weight:700;font-size:17px;line-height:1.05;width:150px}
.brand-square{width:22px;height:22px;background:var(--white);flex:none}
.title{position:absolute;left:250px;top:20px;font-family:"Lilita One",Impact,sans-serif;color:var(--title);
  font-size:40px;line-height:1.05;text-shadow:2px 2px 0 var(--white)}
.photo{position:absolute}
.photo.yacht{left:150px;top:132px;width:400px;height:236px;border-radius:6px;
  background:linear-gradient(180deg,#cfe7f6 0%,#eef6fb 50%,#7fb7dd 100%)}
.photo.crowd{left:530px;top:124px;width:260px;height:230px;border-radius:6px;
  background:linear-gradient(180deg,#b9d6ea 0%,#8fa6b8 60%,#5d7284 100%)}
.photo.host{left:590px;top:720px;width:210px;height:440px;
  background:linear-gradient(180deg,#f0d7c0 0%,#e9e9e9 25%,#d6d6d6 100%);border-radius:40px 40px 8px 8px}
.photo.steamboat{left:330px;top:950px;width:260px;height:220px;border-radius:6px;
  background:linear-gradient(180deg,#f4f1ea 0%,#d8d2c4 60%,#8a8172 100%)}
.card{position:absolute;background:var(--card);border:2px solid var(--card-edge);padding:9px 10px;
  font-size:11px;line-height:1.2}
.day{color:var(--day);font-weight:700;font-size:14.5px;margin:2px 0 5px}
.event{margin-bottom:6px}
.event b{display:block;font-weight:700}
.note{font-weight:700;font-size:12px;margin-top:8px;line-height:1.2}
.c1{left:56px;width:200px}
.c2{left:290px;width:200px}
.c3{left:522px;width:180px}
.r1{top:400px;height:360px}
.r2{top:776px;height:372px}
.r2.c3{height:250px;width:170px}
</style>
</head>
<body>
<div class="poster">
  <div class="brand"><span class="brand-square"></span><span>Granite Ridge College</span></div>

  <h1 class="title">We're at the 'Crest!<br>Welcome Week 2013</h1>

  <div class="photo yacht" role="img" aria-label="Photo of a white yacht on open water"></div>
  <div class="photo crowd" role="img" aria-label="Photo of a group of students posing on deck"></div>
  <div class="photo steamboat" role="img" aria-label="Illustration of a paddle steamboat"></div>
  <div class="photo host" role="img" aria-label="Illustration of a man in a white suit and sunglasses"></div>

  <section class="card c1 r1">
    <h2 class="day">Thursday August 22</h2>
    <p class="event"><b>Residence Hall Move-In</b>12:00pm-5:00pm<br>Hill Hall</p>
    <p class="event"><b>Brunch</b>10:00am-2:00pm<br>Dining Hall</p>
    <p class="event"><b>International Students Orientation</b>3:00pm<br>Bristol 121</p>
    <p class="event"><b>Dinner</b>5:00pm-6:30pm<br>Dining Hall</p>
    <p class="event"><b>Hot Springs Watermelon Party</b>7:00pm-9:00pm<br>Pinecrest Hot Springs</p>
  </section>

  <section class="card c2 r1">
    <h2 class="day">Saturday August 24</h2>
    <p class="event"><b>Main Street Farmers Market</b>9:00am-1:00pm<br>6th &amp; Lincoln (walking dist.)</p>
    <p class="event"><b>Brunch</b>10:00am-1:00pm<br>Dining Hall</p>
    <p class="event"><b>Cedar Park Hot Springs</b>1:00pm-5:00pm<br>Shuttle leaves Hill Hall at 1:30pm</p>
    <p class="event"><b>Dinner</b>5:00-6:30pm<br>Dining Hall</p>
    <p class="event"><b>Free Movie on the Mountain: Summit Trail</b>8:00pm<br>(Shuttle Runs to Resort,<br>9:30pm Last Bus)</p>
  </section>

  <section class="card c3 r1">
    <h2 class="day">Monday August 26</h2>
    <p class="event"><b>Regular Dining Hall Hours Begin</b>"Being Broke Sucks"<br>9:00pm<br>Auditorium</p>
    <h2 class="day">Tuesday August 27</h2>
    <p class="event"><b>Newly Roommate Game</b>7:00pm-8:30pm<br>Hill Hall 109</p>
    <p class="event"><b>Free Gelato</b>8:30pm-9:30pm<br>Class Gelato Hill Patio</p>
    <h2 class="day">Wednesday August 28</h2>
    <p class="event"><b>Free Bowling</b>9:00pm<br>Summit Lanes</p>
  </section>

  <section class="card c1 r2">
    <h2 class="day">Friday August 23</h2>
    <p class="event"><b>Breakfast</b>7:30am-9:00am<br>Dining Hall</p>
    <p class="event"><b>Hike Pine Creek Falls</b>9:00am-11:30am<br>Shuttle leaves Hill Hall at 9am</p>
    <p class="event"><b>BBQ and Faculty Ice Cream Social</b>11:00am-1:00pm<br>Dining Hall</p>
    <p class="event"><b>Kick-Off Party: Inflatables</b>1:30pm-4:00pm<br>Upper Parking Lot</p>
    <p class="event"><b>Dinner</b>5:00pm-6:00pm<br>Dining Hall</p>
    <p class="event"><b>Free Concert</b>7:00pm<br>Pinecrest Resort Base<br>(Shuttle Runs to Resort,<br>9:30pm Last Bus)</p>
  </section>

  <section class="card c2 r2">
    <h2 class="day">Sunday August 25</h2>
    <p class="event"><b>Brunch</b>10:00am-1:00pm<br>Dining Hall</p>
    <p class="event"><b>Alpine Slide/Volleyball</b>2:00pm-4:00pm<br>Meet at Ridge Hill</p>
    <p class="event"><b>Dinner</b>5:00pm-6:30pm<br>Dining Hall</p>
    <p class="event"><b>Mandatory All Hall Meeting</b>8:00pm<br>Auditorium</p>
    <p class="event"><b>RHA Super Sunday Program</b>9:00pm<br>TBD</p>
  </section>

  <section class="card c3 r2">
    <h2 class="day">Thursday August 29</h2>
    <p class="event"><b>Club Fair</b>10:00am-2:00pm<br>Dining Hall</p>
    <p class="event"><b>Black Light Dodgeball</b>9:00pm<br>Gym</p>
    <h2 class="day">Friday August 30</h2>
    <p class="event"><b>Late Night Climbing</b>9:00pm<br>Gym</p>
    <p class="note">ALL EVENTS<br>ARE FREE<br>UNLESS OTHERWISE NOTED</p>
  </section>
</div>
</body>
</html>
```